Business Cards

Business cards (double-sided) to be handed out to clients and potential clients, with contact details, logo .

Target Market(s)

Small to medium size businesses

Industry/Entity Type

Accountants

Contact Information for Business Card

Brightmere Ledger Accounting & Advisory Ltd

Colors

Designer to choose only greyscale colors for use in the design.

Requirements
Must have
• Name, Title, Address, Phone number, Email, Website
Nice to have
• Modern, clean lines, classy
Should not have
• Business cards to be double-sided. Form keeps reverting to single-sided.

```html
<!DOCTYPE html>
<html lang="en">
<head>
<meta charset="utf-8">
<title>Brightmere Ledger — Business Cards</title>
<link rel="stylesheet" href="https://fonts.googleapis.com/css2?family=Open+Sans:wght@300;400;700&display=swap">
<style>
  :root {
    --bg: #1b1b1c;
    --card: #252526;
    --ink: #f2f2f2;
    --ink-soft: #d6d6d6;
    --emboss: #2f2f31;
    --rule: #e6e6e6;
  }
  html, body {
    margin: 0;
    width: 1200px;
    height: 948px;
    overflow: hidden;
    background: var(--bg);
    font-family: "Open Sans", sans-serif;
    color: var(--ink);
  }
  .canvas {
    position: relative;
    width: 1200px;
    height: 948px;
  }
  .card {
    position: absolute;
    top: 326px;
    width: 530px;
    height: 303px;
    background: var(--card);
    border-radius: 22px;
    box-shadow: 0 18px 40px rgba(0,0,0,.45);
    overflow: hidden;
  }
  .card--front { left: 50px; }
  .card--back { left: 620px; }

  .brand-name {
    margin: 0;
    font-weight: 400;
    text-transform: uppercase;
    letter-spacing: .14em;
    line-height: 1.25;
    color: var(--ink);
  }
  .card--front .brand-name {
    position: absolute;
    left: 0; right: 0;
    top: 112px;
    text-align: center;
    font-size: 27px;
  }
  .card--back .brand-name {
    position: absolute;
    left: 34px;
    top: 38px;
    font-size: 15px;
  }
  .brand-name--emboss {
    position: absolute;
    right: 26px;
    top: 38px;
    margin: 0;
    font-size: 15px;
    font-weight: 400;
    text-transform: uppercase;
    letter-spacing: .14em;
    line-height: 1.25;
    text-align: right;
    color: var(--emboss);
  }

  .person {
    position: absolute;
    left: 34px;
    top: 160px;
  }
  .person__name {
    margin: 0;
    font-size: 17px;
    font-weight: 700;
    letter-spacing: .02em;
    text-transform: uppercase;
  }
  .person__title {
    margin: 0;
    font-size: 13px;
    font-weight: 300;
    color: var(--ink-soft);
  }
  .rule {
    position: absolute;
    left: 34px;
    right: 22px;
    top: 208px;
    height: 1px;
    background: var(--rule);
  }
  .contacts {
    position: absolute;
    left: 34px;
    top: 218px;
    margin: 0;
    padding: 0;
    list-style: none;
    font-size: 13px;
    font-weight: 300;
    line-height: 22px;
  }
  .contacts li { display: flex; align-items: center; gap: 8px; }
  .contacts svg { width: 11px; height: 11px; fill: var(--ink); flex: none; }
  .address {
    position: absolute;
    right: 26px;
    top: 222px;
    margin: 0;
    text-align: right;
    font-size: 13px;
    font-weight: 300;
    line-height: 20px;
    font-style: normal;
  }
</style>
</head>
<body>
<main class="canvas">
  <section class="card card--front" aria-label="Card front">
    <p class="brand-name">Brightmere Ledger<br>Accounting &amp; Advisory</p>
  </section>

  <section class="card card--back" aria-label="Card back">
    <p class="brand-name">Brightmere Ledger<br>Accounting &amp; Advisory</p>
    <p class="brand-name--emboss" aria-hidden="true">Brightmere Ledger<br>Accounting &amp; Advisory</p>

    <div class="person">
      <p class="person__name">Daniel Harper</p>
      <p class="person__title">Owner/Ceo</p>
    </div>

    <div class="rule"></div>

    <ul class="contacts">
      <li>
        <svg viewBox="0 0 24 24" aria-hidden="true"><path d="M6.6 10.8a15.1 15.1 0 0 0 6.6 6.6l2.2-2.2a1 1 0 0 1 1-.25 11.4 11.4 0 0 0 3.6.57 1 1 0 0 1 1 1V20a1 1 0 0 1-1 1A17 17 0 0 1 3 4a1 1 0 0 1 1-1h3.5a1 1 0 0 1 1 1c0 1.25.2 2.45.57 3.57a1 1 0 0 1-.25 1z"/></svg>
        555 010 2468
      </li>
      <li>
        <svg viewBox="0 0 24 24" aria-hidden="true"><path d="M2 5h20v14H2z M2 5l10 8 10-8" /></svg>
        hello@brightmereledger.com
      </li>
      <li>
        <svg viewBox="0 0 24 24" aria-hidden="true"><circle cx="12" cy="12" r="10"/></svg>
        www.brightmereledger.com
      </li>
    </ul>

    <address class="address">1480 Harbor Crest Drive<br>Westhaven CA 90214</address>
  </section>
</main>
</body>
</html>
```